Small dedicated blog website

I have recently had a logo designed for my growing personal hobby, I document my adventures around the world in video form (www.vidstream-example.com/marlowventures.com) I am now trying to create a small blog website with easy access to my other social networks to start to create a home base for all the videos and content I create, I would like a simple website with a focus on blog posts and access to my other social networks, instagram (marlowventures), facebook (marlowventures), snapchat (glenmarlow)

My current website can be viewed at www.marlowventures-example.com

Please contact me for any further information to help this project

Many thanks!

I do not expect a fully coded website, simply designs and graphics

Industry/Entity Type

Social

Font styles to use
Sans Serif

Requirements
Must have
• area for tumblr blog placement, access to social media links

```html
<!DOCTYPE html>
<html lang="en">
<head>
<meta charset="utf-8">
<title>Marlow Ventures – Travel Diary</title>
<link rel="stylesheet" href="https://fonts.googleapis.com/css2?family=PT+Sans:ital,wght@0,400;0,700;1,400&display=swap">
<style>
:root{
  --sidebar:#2f2f2f;
  --sidebar-line:#3a3a3a;
  --nav-active:#3b3b3b;
  --text-light:#e9e9e9;
  --text-muted:#bcbcbc;
  --page:#ffffff;
  --card-border:#e3e3e3;
  --title:#2b2b2b;
  --date:#9a9a9a;
  --body:#4a4a4a;
  --stat:#9f9f9f;
  --stat-faint:#d6d6d6;
  --player:#000000;
  --slider:#4a4a4a;
}
*{box-sizing:border-box;margin:0;padding:0}
html,body{width:1200px;height:900px;overflow:hidden;background:var(--page);font-family:"PT Sans",sans-serif}
.site{display:flex;width:1200px;height:900px}
.sidebar{width:194px;background:var(--sidebar);color:var(--text-light);flex-shrink:0}
.brand{display:flex;flex-direction:column;align-items:center;padding-top:26px}
.brand-mark{width:44px;height:44px;border-radius:50%;background:#e6e6e6}
.brand-name{margin-top:14px;font-size:10px;font-weight:700;letter-spacing:.3px}
.avatar{width:116px;height:116px;border-radius:50%;margin:28px auto 0;background:radial-gradient(circle at 50% 45%,#d8b49a,#8b7a6e 60%,#4b4b4b)}
.tagline{margin:18px 14px 0;text-align:center;font-style:italic;font-size:11.5px;line-height:17px;color:var(--text-muted)}
.social{display:flex;justify-content:center;gap:24px;margin-top:16px}
.social span{width:18px;height:18px;border-radius:50%;background:#f2f2f2}
.search{margin:26px 7px 7px;height:22px;background:#f4f4f4;border:1px solid #cfcfcf;display:flex;align-items:center;padding-left:6px;gap:5px;font-size:8px;color:#9a9a9a}
.nav{list-style:none}
.nav li{height:31px;border-bottom:1px solid var(--sidebar-line);display:flex;align-items:center;gap:10px;padding-left:9px;font-size:10px}
.nav li.active{background:var(--nav-active)}
.nav svg{width:16px;height:14px}
.feed{display:flex;gap:22px;padding:22px 0 0 22px}
.column{width:307px;display:flex;flex-direction:column;gap:22px}
.card{border:1px solid var(--card-border);background:#fff}
.media{display:block;width:100%}
.card-body{padding:11px 28px 16px}
.card-title{font-size:18px;font-weight:400;color:var(--title);line-height:24px}
.card-date{font-size:9.5px;color:var(--date);margin-top:3px}
.card-text{margin-top:13px;font-size:10.5px;line-height:14px;color:var(--body);letter-spacing:.5px;text-align:justify}
.stats{display:flex;justify-content:space-between;margin-top:17px;font-size:12px}
.stat{display:flex;align-items:center;gap:8px;color:var(--stat)}
.stat.faint{color:var(--stat-faint)}
.dot{width:10px;height:14px;background:var(--stat-faint)}
.dot.round{width:16px;height:14px;border-radius:50%}
.video-bar{height:33px;background:#1a1a1a;display:flex;align-items:center;gap:12px;padding:0 16px}
.video-track{flex:1;height:6px;background:#444;position:relative}
.video-track i{position:absolute;left:0;top:0;height:6px;width:35%;background:#ddd}
.audio{background:var(--player);color:#fff}
.audio-info{padding:20px 28px 0;height:85px}
.audio-track{font-size:16px}
.audio-time{font-size:12.5px;margin-top:4px}
.audio-progress{height:5px;background:#333}
.audio-progress i{display:block;width:40px;height:5px;background:#bbb}
.audio-controls{height:34px;display:flex;align-items:center;justify-content:space-between;padding:0 36px}
.slider-caption{position:absolute;left:0;right:0;bottom:43px;height:24px;background:rgba(40,40,40,.55);color:#fff;font-size:13px;padding-left:12px;line-height:24px}
.slider-bar{position:absolute;left:0;right:0;bottom:0;height:43px;background:var(--slider);display:flex;align-items:center;justify-content:space-between;padding:0 10px}
.dots{display:flex;gap:8px}
.dots span{width:9px;height:9px;border-radius:50%;background:#fff}
.dots span.off{background:transparent;border:1.5px solid #fff}
.gallery{position:relative;height:292px;background:linear-gradient(135deg,#8a7a80,#5e5257 60%,#3d3a3b)}
</style>
</head>
<body>
<div class="site">
  <aside class="sidebar">
    <div class="brand">
      <span class="brand-mark"></span>
      <div class="brand-name">MARLOWVENTURES.COM</div>
    </div>
    <div class="avatar" role="img" aria-label="Portrait of the blogger wearing sunglasses"></div>
    <p class="tagline">I am tri-citizen of our beautiful planet and this is my diary of various adventures recent relocation of Finland</p>
    <div class="social"><span></span><span></span><span></span></div>
    <div class="search">
      <svg width="8" height="8" viewBox="0 0 8 8"><circle cx="3.2" cy="3.2" r="2.4" fill="none" stroke="#999"/><path d="M5 5l2.5 2.5" stroke="#999"/></svg>Search
    </div>
    <ul class="nav">
      <li class="active"><svg viewBox="0 0 16 14"><path d="M1 7q7-8 14 0q-7 8-14 0z" fill="none" stroke="#eee" stroke-width="1.3"/><circle cx="8" cy="7" r="2.3" fill="none" stroke="#eee" stroke-width="1.3"/></svg>All Posts</li>
      <li><svg viewBox="0 0 16 14"><rect x="1" y="1" width="14" height="12" fill="none" stroke="#ccc"/><path d="M4 1v12M12 1v12M1 4h3M1 7h3M1 10h3M12 4h3M12 7h3M12 10h3" stroke="#ccc"/></svg>Video</li>
      <li><svg viewBox="0 0 16 14"><rect x="1" y="1" width="14" height="12" fill="none" stroke="#ccc"/><path d="M2 11l4-4 3 3 2-2 3 3" fill="none" stroke="#ccc"/></svg>Photos</li>
      <li><svg viewBox="0 0 16 14"><path d="M1 5h3l4-3v10l-4-3H1z" fill="#ccc"/><path d="M10 4q2 3 0 6M12 2q4 5 0 10" fill="none" stroke="#ccc"/></svg>Audios</li>
      <li><svg viewBox="0 0 16 14"><rect x="1" y="1" width="14" height="12" fill="none" stroke="#ccc"/><path d="M3 4h4v4H3zM9 4h4M9 6h4M9 8h4M3 10h10" stroke="#ccc" fill="none"/></svg>Blogs</li>
    </ul>
  </aside>

  <main class="feed">
    <section class="column">
      <article class="card">
        <div class="media" style="height:171px;background:linear-gradient(160deg,#f3e1d2,#e8cdb8)" role="img" aria-label="Close-up of a travel insurance card"></div>
        <div class="card-body">
          <h2 class="card-title">Title for your news blog</h2>
          <div class="card-date">12 April 2014</div>
          <p class="card-text">Lorem ipsum dolor sit amet, consectetur adipiscing elit. Sed condimentum aliquet venenatis. Etiam a nisi nunc, a tincidunt eros.</p>
          <div class="stats">
            <span class="stat"><svg width="16" height="15" viewBox="0 0 16 15"><path d="M0 0h16v11H5l-4 4v-4H0z" fill="#bdbdbd"/></svg>221</span>
            <span class="stat faint"><i class="dot"></i>359</span>
            <span class="stat faint"><i class="dot round"></i>741</span>
          </div>
        </div>
      </article>
      <article class="card">
        <div class="gallery" role="img" aria-label="Photo of folded knitted blankets">
          <div class="slider-caption">Lorem ipsum dolor sit amet</div>
          <div class="slider-bar">
            <svg width="16" height="30" viewBox="0 0 16 30"><path d="M15 1L1 15l14 14" fill="none" stroke="#ddd" stroke-width="1.4"/></svg>
            <div class="dots"><span></span><span class="off"></span><span></span><span></span></div>
            <svg width="16" height="30" viewBox="0 0 16 30"><path d="M1 1l14 14L1 29" fill="none" stroke="#ddd" stroke-width="1.4"/></svg>
          </div>
        </div>
        <div class="card-body">
          <h2 class="card-title">Title for your photos</h2>
          <div class="card-date">12 April 2014</div>
          <div class="stats">
            <span class="stat"><svg width="16" height="15" viewBox="0 0 16 15"><path d="M0 0h16v11H5l-4 4v-4H0z" fill="#bdbdbd"/></svg>221</span>
            <span class="stat faint"><i class="dot"></i>359</span>
            <span class="stat faint"><i class="dot round"></i>741</span>
          </div>
        </div>
      </article>
    </section>

    <section class="column">
      <article class="card">
        <div class="media" style="height:216px;background:linear-gradient(180deg,#d9dde2,#e7d7a8 45%,#9c9f98)" role="img" aria-label="Video still of a yellow apartment building in winter"></div>
        <div class="video-bar">
          <svg width="10" height="12" viewBox="0 0 10 12"><path d="M0 0l10 6-10 6z" fill="#fff"/></svg>
          <div class="video-track"><i></i></div>
          <svg width="14" height="14" viewBox="0 0 14 14"><path d="M1 13L13 1M8 1h5v5M1 8v5h5" fill="none" stroke="#888" stroke-width="1.3"/></svg>
        </div>
        <div class="card-body">
          <h2 class="card-title">Title for your video</h2>
          <div class="card-date">12 April 2014</div>
          <div class="stats">
            <span class="stat"><svg width="16" height="15" viewBox="0 0 16 15"><path d="M0 0h16v11H5l-4 4v-4H0z" fill="#bdbdbd"/></svg>221</span>
            <span class="stat faint"><i class="dot"></i>359</span>
            <span class="stat faint"><i class="dot round"></i>741</span>
          </div>
        </div>
      </article>
      <article class="card">
        <div class="media" style="height:171px;background:linear-gradient(135deg,#cfcfcb,#f1efe8 55%,#3a3a38)" role="img" aria-label="Living room with white sofa and dark tables"></div>
        <div class="card-body">
          <h2 class="card-title">Title for your news blog</h2>
          <div class="card-date">12 April 2014</div>
          <p class="card-text">Lorem ipsum dolor sit amet, consectetur adipiscing elit. Sed condimentum aliquet venenatis. Etiam a nisi nunc, a tincidunt eros.</p>
          <div class="stats">
            <span class="stat"><svg width="16" height="15" viewBox="0 0 16 15"><path d="M0 0h16v11H5l-4 4v-4H0z" fill="#bdbdbd"/></svg>221</span>
            <span class="stat faint"><i class="dot"></i>359</span>
            <span class="stat faint"><i class="dot round"></i>741</span>
          </div>
        </div>
      </article>
    </section>

    <section class="column">
      <article class="card">
        <div class="audio">
          <div class="audio-info">
            <div class="audio-track">Track 1</div>
            <div class="audio-time">01:00</div>
          </div>
          <div class="audio-progress"><i></i></div>
          <div class="audio-controls">
            <svg width="30" height="12" viewBox="0 0 30 12"><path d="M0 1h2v10H0zM2 6l7-5v10zM13 6l7-5v10zM20 6l7-5v10z" fill="#fff"/></svg>
            <svg width="32" height="32" viewBox="0 0 32 32"><circle cx="16" cy="16" r="14" fill="none" stroke="#fff" stroke-width="2.5"/><path d="M12 10h3v12h-3zM17 10h3v12h-3z" fill="#fff"/></svg>
            <svg width="30" height="12" viewBox="0 0 30 12"><path d="M0 1l7 5-7 5zM7 1l7 5-7 5zM19 1l7 5-7 5zM28 1h2v10h-2z" fill="#fff"/></svg>
          </div>
        </div>
        <div class="card-body">
          <h2 class="card-title">Title for your audio</h2>
          <div class="card-date">12 April 2014</div>
          <div class="stats">
            <span class="stat"><svg width="16" height="15" viewBox="0 0 16 15"><path d="M0 0h16v11H5l-4 4v-4H0z" fill="#bdbdbd"/></svg>221</span>
            <span class="stat faint"><i class="dot"></i>359</span>
            <span class="stat faint"><i class="dot round"></i>741</span>
          </div>
        </div>
      </article>
      <article class="card">
        <div class="media" style="height:171px;background:linear-gradient(135deg,#e9e9e6,#f7f6f2 50%,#6b5040)" role="img" aria-label="White kitchen with wooden worktop and armchair"></div>
        <div class="card-body">
          <h2 class="card-title">Title for your news blog</h2>
          <div class="card-date">12 April 2014</div>
          <p class="card-text">Lorem ipsum dolor sit amet, consectetur adipiscing elit. Sed condimentum aliquet venenatis. Etiam a nisi nunc, a tincidunt eros.</p>
          <div class="stats">
            <span class="stat"><svg width="16" height="15" viewBox="0 0 16 15"><path d="M0 0h16v11H5l-4 4v-4H0z" fill="#bdbdbd"/></svg>221</span>
            <span class="stat faint"><i class="dot"></i>359</span>
            <span class="stat faint"><i class="dot round"></i>741</span>
          </div>
        </div>
      </article>
    </section>
  </main>
</div>
</body>
</html>
```